2 Redfern Pike Auto Care Banners

Looking to have two pull up banners designed - each 33.5 x 80

First banner- Scheduled Maintenance, Diagnostics, Inspections
Voted Top Pick Marbury 3 years in a row!

Second banner- Brakes, Tires, General Auto Service
Include the 3 TPM logos
2019, 2018, 2017

```html
<!DOCTYPE html>
<html lang="en">
<head>
<meta charset="utf-8">
<title>Redfern Pike Auto Care – Pull Up Banners</title>
<link href="https://fonts.googleapis.com/css2?family=Fjalla+One&family=Questrial&display=swap" rel="stylesheet">
<style>
  :root {
    --navy: #3f4a72;
    --gold: #c2b85c;
    --white: #f4f4f4;
    --black: #000000;
    --stage: #e4e4e4;
    --car-blue: #2f6fd6;
    --car-deep: #0f3d9a;
    --tire-dark: #141414;
    --tire-mid: #3a3a3a;
  }
  * { box-sizing: border-box; margin: 0; padding: 0; }
  html, body { width: 1200px; height: 973px; overflow: hidden; }
  body {
    background: radial-gradient(ellipse at 50% 45%, #f0f0f0 0%, var(--stage) 60%, #d4d4d4 100%);
    position: relative;
    font-family: "Fjalla One", "Arial Narrow", sans-serif;
  }
  .banner {
    position: absolute;
    top: 128px;
    width: 300px;
    height: 716px;
    overflow: hidden;
    box-shadow: 0 12px 30px rgba(0,0,0,0.18);
  }
  .banner--services { left: 170px; }
  .banner--repairs { left: 730px; }
  .banner__art { position: absolute; inset: 0; width: 300px; height: 716px; display: block; }
  .brand {
    position: absolute; top: 22px; left: 0; width: 100%;
    text-align: center;
  }
  .brand__name {
    font-family: "Fjalla One", sans-serif;
    color: var(--gold);
    font-size: 38px;
    letter-spacing: 1px;
    line-height: 1;
  }
  .brand__tagline {
    margin-top: 14px;
    font-family: "Questrial", sans-serif;
    color: var(--white);
    font-size: 12px;
    letter-spacing: 3px;
  }
  .services {
    position: absolute; left: 0; width: 100%;
    text-align: center;
    text-transform: uppercase;
  }
  .banner--services .services { top: 170px; color: var(--navy); }
  .banner--repairs .services { top: 176px; color: var(--white); }
  .services__item { font-size: 27px; line-height: 1.22; letter-spacing: 0.5px; }
  .services__stars {
    color: var(--gold); font-size: 9px; letter-spacing: 12px;
    padding-left: 12px; margin: 14px 0 16px;
  }
  .award {
    position: absolute; left: 20px; bottom: 22px;
    display: flex; align-items: center; gap: 14px;
  }
  .award__text {
    font-family: "Questrial", sans-serif; color: var(--white);
    font-size: 15px; line-height: 1.2; text-align: right;
  }
  .award__badge { width: 50px; height: 32px; background: var(--white); }
  .website {
    position: absolute; bottom: 30px; left: 0; width: 100%;
    text-align: center;
    font-family: "Questrial", sans-serif; color: var(--white);
    font-size: 20px; letter-spacing: 0.5px;
  }
</style>
</head>
<body>

<section class="banner banner--services">
  <svg class="banner__art" viewBox="0 0 300 716" aria-hidden="false">
    <defs>
      <linearGradient id="carTones" x1="0" y1="0" x2="0" y2="1">
        <stop offset="0" stop-color="var(--white)"/>
        <stop offset="0.25" stop-color="var(--car-blue)"/>
        <stop offset="1" stop-color="var(--car-deep)"/>
      </linearGradient>
    </defs>
    <rect class="panel-navy" width="300" height="716" fill="var(--navy)"/>
    <path class="band-gold" d="M0,180 C80,122 200,104 300,108 L300,716 L0,716 Z" fill="var(--gold)"/>
    <path class="panel-white" d="M0,194 C90,142 200,128 300,134 L300,716 L0,716 Z" fill="var(--white)"/>
    <path class="photo-car" role="img" aria-label="Photo of a blue sedan seen from the front"
          d="M0,410 L300,410 L300,555 C200,600 100,622 0,628 Z" fill="url(#carTones)"/>
    <path class="band-gold" d="M0,628 C100,622 200,600 300,555 L300,716 L0,716 Z" fill="var(--gold)"/>
    <path class="panel-navy" d="M0,650 C100,646 200,628 300,578 L300,716 L0,716 Z" fill="var(--navy)"/>
  </svg>

  <header class="brand">
    <div class="brand__name">Redfern Pike</div>
    <div class="brand__tagline">COMPLETE AUTO CARE</div>
  </header>

  <div class="services">
    <div class="services__item">Scheduled<br>Maintenance</div>
    <div class="services__stars">★★★★★</div>
    <div class="services__item">Diagnostics</div>
    <div class="services__stars">★★★★★</div>
    <div class="services__item">Inspections</div>
  </div>

  <div class="award">
    <p class="award__text">Voted Top Pick Marbury<br>3 years in a row!</p>
    <div class="award__badge" role="img" aria-label="Top Pick Marbury award badge"></div>
  </div>
</section>

<section class="banner banner--repairs">
  <svg class="banner__art" viewBox="0 0 300 716">
    <defs>
      <radialGradient id="tireTones" cx="0.6" cy="0.4" r="0.8">
        <stop offset="0" stop-color="var(--tire-mid)"/>
        <stop offset="1" stop-color="var(--tire-dark)"/>
      </radialGradient>
    </defs>
    <rect class="panel-navy" width="300" height="716" fill="var(--navy)"/>
    <path class="band-gold" d="M0,200 C90,140 200,118 300,120 L300,716 L0,716 Z" fill="var(--gold)"/>
    <path class="panel-black" d="M0,214 C90,158 200,140 300,146 L300,716 L0,716 Z" fill="var(--black)"/>
    <path class="photo-tires" role="img" aria-label="Photo of two stacked car tires on a dark background"
          d="M0,420 L300,420 L300,595 C220,625 120,640 0,642 Z" fill="url(#tireTones)"/>
    <path class="band-gold" d="M0,642 C120,640 220,625 300,595 L300,716 L0,716 Z" fill="var(--gold)"/>
    <path class="panel-navy" d="M0,664 C120,660 220,642 300,612 L300,716 L0,716 Z" fill="var(--navy)"/>
  </svg>

  <header class="brand">
    <div class="brand__name">Redfern Pike</div>
    <div class="brand__tagline">COMPLETE AUTO CARE</div>
  </header>

  <div class="services">
    <div class="services__item">Brakes</div>
    <div class="services__stars">★★★★★</div>
    <div class="services__item">Tires</div>
    <div class="services__stars">★★★★★</div>
    <div class="services__item">General Auto<br>Service</div>
  </div>

  <p class="website">www.redfernpikeauto.com</p>
</section>

</body>
</html>
```